Corvane Building Materials letterhead template

Simple but professional letterhead template for business communication.
LOGO/name in upper left, balanced by company contact info on right upper.
Subject description, date...
addressee, cc: and BC: if applicable editable info..

Need extra days to review

```html
<!DOCTYPE html>
<html lang="en">
<head>
<meta charset="utf-8">
<title>Corvane Building Materials – Letterhead</title>
<link rel="stylesheet" href="https://fonts.googleapis.com/css2?family=Open+Sans:wght@400;800&family=Montserrat:wght@400&display=swap">
<style>
  :root {
    --brand-blue: #0a5cc2;
    --ink: #1a1a1a;
    --paper: #ffffff;
    --backdrop: #eceded;
  }
  * { margin: 0; padding: 0; box-sizing: border-box; }
  html, body { width: 1200px; height: 960px; overflow: hidden; }
  body {
    background: var(--backdrop);
    font-family: "Open Sans", Tahoma, sans-serif;
    color: var(--ink);
  }
  .letterhead {
    position: absolute;
    left: 275px; top: 20px;
    width: 650px; height: 920px;
    background: var(--paper);
    box-shadow: 0 4px 18px rgba(0,0,0,0.12);
    overflow: hidden;
  }
  .band { position: absolute; left: 0; width: 100%; }
  .band--top { top: 0; height: 40px; }
  .band--bottom { bottom: 0; height: 60px; }
  .band path { fill: var(--brand-blue); }

  .masthead {
    position: absolute; left: 40px; right: 40px; top: 62px;
    display: flex; justify-content: space-between; align-items: center;
  }
  .brand { display: flex; align-items: center; gap: 10px; }
  .brand__mark {
    width: 30px; height: 30px; border-radius: 6px;
    background: var(--brand-blue);
  }
  .brand__name {
    font-weight: 800; font-size: 12px; line-height: 1.05;
    color: var(--brand-blue); text-transform: uppercase; letter-spacing: 0.6px;
  }

  .contact {
    display: flex; flex-direction: column; align-items: flex-end; gap: 6px;
    font-family: "Montserrat", Arial, sans-serif; font-size: 11px;
    color: var(--brand-blue);
  }
  .contact__item { display: flex; align-items: center; gap: 8px; }
  .contact__item::before {
    content: ""; width: 9px; height: 9px; border-radius: 50%;
    background: var(--brand-blue);
  }

  .letter {
    position: absolute; left: 95px; top: 140px; width: 500px;
    font-size: 10.5px; line-height: 1.45; text-transform: uppercase;
    letter-spacing: 0.1px;
  }
  .letter p { margin-bottom: 16px; }
  .letter .signoff { margin-top: 22px; }
</style>
</head>
<body>
  <main class="letterhead">
    <svg class="band band--top" viewBox="0 0 650 40" preserveAspectRatio="none" aria-hidden="true">
      <path d="M0 0 H350 V10 H0 Z"/>
      <path d="M160 0 H350 L330 30 H200 L185 22 H160 Z"/>
      <path d="M355 0 H430 L405 20 H335 Z"/>
      <path d="M440 0 H650 V6 L520 6 L505 16 H420 Z"/>
    </svg>

    <header class="masthead">
      <div class="brand">
        <span class="brand__mark"></span>
        <span class="brand__name">Corvane<br>Building<br>Materials</span>
      </div>
      <address class="contact" style="font-style: normal;">
        <span class="contact__item">0400 555 019</span>
        <span class="contact__item">hello@corvanebuild.com</span>
      </address>
    </header>

    <section class="letter">
      <p>[Your Company Name]<br>[Your Address]<br>[City, State, ZIP Code]<br>[Your Email] | [Your Phone Number]<br>[Date]</p>
      <p>To: [Recipient's Name]<br>[Recipient's Position]<br>[Company/Organization Name]<br>[Address]<br>[City, State, ZIP Code]</p>
      <p>CC: [Optional – Name(s) of other recipients]<br>BC: [Optional – Name(s) of hidden recipients]</p>
      <p>Subject: [Your Subject Here]</p>
      <p>Dear [Recipient's Name],</p>
      <p>I hope this letter finds you well. I am writing to [briefly state the purpose of the letter]. [Provide more details about the main point, such as explaining a request, sharing important information, or giving an update.]</p>
      <p>[Include any necessary supporting information, background context, or next steps. If any action is required from the recipient, specify it clearly.]</p>
      <p>Please feel free to contact me at your earliest convenience should you have any questions or require further clarification. I appreciate your time and look forward to your response.</p>
      <p class="signoff">Best regards,<br>[Your Name]<br>[Your Position]<br>[Your Company/Organization Name]</p>
    </section>

    <svg class="band band--bottom" viewBox="0 0 650 60" preserveAspectRatio="none" aria-hidden="true">
      <path d="M0 60 V22 H90 L100 30 H220 L210 46 H650 V60 Z"/>
      <path d="M95 24 L112 8 H180 L165 24 Z"/>
      <path d="M172 22 L200 0 H270 L245 22 Z"/>
    </svg>
  </main>
</body>
</html>
```